14 years in business and its time for a new look and feel brochure and business cards!

We are looking to create a brochure that is professional and eye catching to bring in new commercial business. After14 years in business we have finally redone our logo and it is time to get a brochure completed as well. The logo that should be used is the one that says Inc. We want this new brochure to appeal to corporate property management companies and smaller apartment complexes. We want it to look rich and have the same high quality our work has.

Target Market(s)

property management companies and apartment complexes in the DMV.

Industry/Entity Type

Construction Company

Contact Information for Business Card

Logo
Dovid Rennick
CEO
Mobile 410-555-0137
Office 410-555-0192
Address 3817 Larchmont Lane Suite B Baltimore, MD 21208
Email DR@BrightCoatInc.example

Font styles to use
Sans Serif

Requirements
Must have
• Want the background to be black and silver gradient. Will be printing on high gloss and would like for it to be rich looking.
• brochure will be 8.5x11. open minded in terms of the fold, how it looks best with the design provided will determine that. Can be bi-fold, try-fold or z-fold.
• Content for brochure:About us
• Founded in 2003, The Bright Coat Inc. was the vision of Dovid Rennick, with a commitment to becoming the premier renovator and developer of residential and commercial properties in the DMV. Today, The Bright Coat Inc. is widely respected for their gold standard in quality and efficiency and continues to grow by attracting the highest level of professionals with knowledge and experience in our field.
• The Bright Coat Inc.’s most valuable asset is our team members. The efforts they put forth are the key to meeting our standards and providing all of our valued clients with the highest quality of service. Leading our wonderful team members is a group of management like no other. With years of experience, the power to motivate and the keen eye to ensure top quality, our team of experts focus all of their energy to exceed our client’s expectations.
• Our Mission
• We strive to provide timely delivery, the highest level of quality and value on every project. We offer unsurpassed dedication to maintain our working relationships and consistently deliver the best service to ensure our clients success.
• Property Renovations
• The Bright Coat Inc. has been responsible for coordinating the construction and renovation of many projects, including all parts of a building’s interior and exterior. Well known for attention to details, quality and timely execution, The Bright Coat Inc. has managed and executed more than 4,000 turnovers and over 150 projects in the last 3 years alone.
• Renovations not only improve the appeal and marketability of your property, but also add value. Interior and exterior renovations help make any property more functional, energy-efficient and enable you to keep up with what your market demands. From the smallest change of a door knob to a complete kitchen overhaul, these are the things that make all the difference in your property. We are committed to deliver great value, and we do that by ensuring that our experts are involved in the renovation process, providing input and quality maintenance throughout the entire renovation.
• Services Include
• Painting
• Flooring
• Sub-Flooring
• Crown molding
• Siding & Wood Replacement
• Trim & Carpentry Work
• Punches
• Decks
• Power wash
• Concrete & Paving
• Turnovers including plumbing and electric
• Kitchen overhauls
• We offer first time clients a free apartment paint or punch on us to show you the quality you can always expect!
• Call today to schedule your first-time paint or punch at 410-555-0192.

```html
<!DOCTYPE html>
<html lang="en">
<head>
<meta charset="utf-8">
<title>The Bright Coat Inc. – Brochure</title>
<link href="https://fonts.googleapis.com/css2?family=Lato:wght@400;700&family=Orbitron:wght@900&display=swap" rel="stylesheet">
<style>
  :root{
    --stage:#242424;
    --ink:#4a4a4a;
    --heading:#555555;
    --white:#ffffff;
    --paper-light:#ffffff;
    --paper-grey:#c9c9c9;
    --photo-light:#b9b2ac;
    --photo-mid:#6e4a3c;
    --photo-dark:#1c1a19;
  }
  *{margin:0;padding:0;box-sizing:border-box}
  html,body{width:1200px;height:801px;overflow:hidden;background:var(--stage)}
  body{position:relative;font-family:"Lato",Arial,sans-serif;color:var(--ink)}
  .spread{position:absolute;left:60px;top:50px;width:1079px;height:698px;overflow:hidden}
  .hero{position:absolute;left:0;top:0;width:1079px;height:361px;overflow:hidden}
  .hero-photo{position:absolute;inset:0;
    background:
      linear-gradient(180deg,rgba(0,0,0,0) 55%,rgba(0,0,0,.35) 100%),
      linear-gradient(100deg,var(--photo-light) 0%,#d9d4cf 18%,var(--photo-mid) 32%,var(--photo-dark) 36%,#2a2523 70%,#161514 100%);}
  .hero-brand{position:absolute;left:733px;top:70px;width:180px;text-align:center;color:var(--white);
    font-weight:700;font-size:20px;line-height:1.2;display:flex;flex-direction:column;align-items:center;gap:8px}
  .hero-brand .dot{width:54px;height:54px;border-radius:50%;background:var(--white)}
  .cta{position:absolute;left:597px;top:203px;width:453px;height:73px;border:1.5px solid var(--white);border-radius:8px;border-top:none}
  .cta::before,.cta::after{content:"";position:absolute;top:0;height:1.5px;background:var(--white);width:32px}
  .cta::before{left:0}.cta::after{right:0}
  .cta-line{position:absolute;top:-8px;left:0;right:0;text-align:center;color:var(--white);font-weight:700;font-size:12.8px}
  .cta-phone{position:absolute;top:22px;left:0;right:0;text-align:center;color:var(--white);
    font-family:"Orbitron",Arial,sans-serif;font-weight:900;font-size:38px;letter-spacing:1px;line-height:1}
  .panel{position:absolute;top:361px;height:337px;overflow:hidden}
  .panel-left{left:0;width:539px;background:linear-gradient(90deg,var(--paper-light) 0%,var(--paper-light) 70%,var(--paper-grey) 100%)}
  .panel-right{left:539px;width:540px;background:linear-gradient(90deg,var(--paper-light) 0%,var(--paper-light) 60%,var(--paper-grey) 100%)}
  .section-title{position:absolute;font-weight:700;font-size:13.5px;color:var(--heading);display:flex;align-items:center;gap:7px}
  .section-title svg{width:13px;height:12px}
  .copy{position:absolute;font-size:10px;line-height:12.75px}
  .copy p+p{margin-top:12.75px}
  .justify{text-align:justify}
  .interior-photo{position:absolute;left:307px;top:157px;width:194px;height:140px;
    background:linear-gradient(180deg,#e9e9e9 0%,#d8d6d3 60%,#9b8f86 100%)}
  .services-title{position:absolute;left:26px;top:195px;font-weight:700;font-size:13.5px;color:var(--heading)}
  .services{position:absolute;top:222px;list-style:none;font-size:10px;line-height:12.8px}
  .services li{display:flex;align-items:center;gap:8px}
  .services svg{width:7px;height:7px;flex:none}
  .footer-brand{position:absolute;left:420px;top:205px;width:100px;text-align:center;color:#5a5a5a;font-weight:700;font-size:13px;line-height:1.2;display:flex;flex-direction:column;align-items:center;gap:6px}
  .footer-brand .dot{width:36px;height:36px;border-radius:50%;background:#6a6a6a}
</style>
</head>
<body>
<main class="spread">
  <section class="hero">
    <div class="hero-photo" role="img" aria-label="Row of brick and white-rendered suburban houses, darkened toward the right"></div>
    <div class="hero-brand"><span class="dot"></span><span>The Bright Coat Inc.</span></div>
    <div class="cta">
      <p class="cta-line">Call today to schedule your first-time paint or punch at</p>
      <p class="cta-phone">410-555-0192</p>
    </div>
  </section>

  <section class="panel panel-left">
    <h2 class="section-title" style="left:29px;top:20px"><svg viewBox="0 0 13 12"><path d="M1 1l5 5-5 5M6 1l5 5-5 5" fill="none" stroke="#555" stroke-width="2"/></svg>About us</h2>
    <div class="copy justify" style="left:29px;top:42px;width:230px">
      <p>Founded in 2003, The Bright Coat Inc. was the vision of Dovid Rennick, with a commitment to becoming the premier renovator and developer of residential and commercial properties in the DMV. Today, The Bright Coat Inc. is widely respected for their gold standard in quality and efficiency and continues to grow by attracting the highest level of professionals with knowledge and experience in our field.</p>
      <p>The Bright Coat Inc.’s most valuable asset is our team members. The efforts they put forth are the key to meeting our standards and providing all of our valued clients with the highest quality of service. Leading our wonderful team members is a group of management like no other. With years of experience, the power to motivate and the keen eye to ensure top quality, our team of experts focus all of their energy to exceed our client’s expectations.</p>
    </div>
    <h2 class="section-title" style="left:307px;top:20px"><svg viewBox="0 0 13 12"><path d="M1 1l5 5-5 5M6 1l5 5-5 5" fill="none" stroke="#555" stroke-width="2"/></svg>Our Mission</h2>
    <div class="copy justify" style="left:307px;top:42px;width:194px">
      <p>We strive to provide timely delivery, the highest level of quality and value on every project. We offer unsurpassed dedication to maintain our working relationships and consistently deliver the best service to ensure our clients success.</p>
    </div>
    <div class="interior-photo" role="img" aria-label="Bright modern living room with fireplace, pendant lamps and dark sofa"></div>
  </section>

  <section class="panel panel-right">
    <h2 class="section-title" style="left:26px;top:20px"><svg viewBox="0 0 13 12"><path d="M1 1l5 5-5 5M6 1l5 5-5 5" fill="none" stroke="#555" stroke-width="2"/></svg>Property Renovations</h2>
    <div class="copy" style="left:26px;top:42px;width:489px">
      <p>The Bright Coat Inc. has been responsible for coordinating the construction and renovation of many projects, including all parts of a building’s interior and exterior. Well known for attention to details, quality and timely execution, The Bright Coat Inc. has managed and executed more than 4,000 turnovers and over 150 projects in the last 3 years alone.</p>
      <p>Renovations not only improve the appeal and marketability of your property, but also add value. Interior and exterior renovations help make any property more functional, energy-efficient and enable you to keep up with what your market demands. From the smallest change of a door knob to a complete kitchen overhaul, these are the things that make all the difference in your property. We are committed to deliver great value, and we do that by ensuring that our experts are involved in the renovation process, providing input and quality maintenance throughout the entire renovation</p>
    </div>
    <h3 class="services-title">Services Include</h3>
    <ul class="services" style="left:26px">
      <li><svg viewBox="0 0 7 7"><path d="M0 0l3 3.5L0 7M3.5 0l3 3.5-3 3.5" fill="none" stroke="#555" stroke-width="1.3"/></svg>Painting</li>
      <li><svg viewBox="0 0 7 7"><path d="M0 0l3 3.5L0 7M3.5 0l3 3.5-3 3.5" fill="none" stroke="#555" stroke-width="1.3"/></svg>Flooring</li>
      <li><svg viewBox="0 0 7 7"><path d="M0 0l3 3.5L0 7M3.5 0l3 3.5-3 3.5" fill="none" stroke="#555" stroke-width="1.3"/></svg>Sub-Flooring</li>
      <li><svg viewBox="0 0 7 7"><path d="M0 0l3 3.5L0 7M3.5 0l3 3.5-3 3.5" fill="none" stroke="#555" stroke-width="1.3"/></svg>Crown molding</li>
      <li><svg viewBox="0 0 7 7"><path d="M0 0l3 3.5L0 7M3.5 0l3 3.5-3 3.5" fill="none" stroke="#555" stroke-width="1.3"/></svg>Siding &amp; Wood Replacement</li>
      <li><svg viewBox="0 0 7 7"><path d="M0 0l3 3.5L0 7M3.5 0l3 3.5-3 3.5" fill="none" stroke="#555" stroke-width="1.3"/></svg>Trim &amp; Carpentry Work</li>
    </ul>
    <ul class="services" style="left:199px">
      <li><svg viewBox="0 0 7 7"><path d="M0 0l3 3.5L0 7M3.5 0l3 3.5-3 3.5" fill="none" stroke="#555" stroke-width="1.3"/></svg>Punches</li>
      <li><svg viewBox="0 0 7 7"><path d="M0 0l3 3.5L0 7M3.5 0l3 3.5-3 3.5" fill="none" stroke="#555" stroke-width="1.3"/></svg>Decks</li>
      <li><svg viewBox="0 0 7 7"><path d="M0 0l3 3.5L0 7M3.5 0l3 3.5-3 3.5" fill="none" stroke="#555" stroke-width="1.3"/></svg>Power wash</li>
      <li><svg viewBox="0 0 7 7"><path d="M0 0l3 3.5L0 7M3.5 0l3 3.5-3 3.5" fill="none" stroke="#555" stroke-width="1.3"/></svg>Concrete &amp; Paving</li>
      <li><svg viewBox="0 0 7 7"><path d="M0 0l3 3.5L0 7M3.5 0l3 3.5-3 3.5" fill="none" stroke="#555" stroke-width="1.3"/></svg>Turnovers including plumbing and electric</li>
      <li><svg viewBox="0 0 7 7"><path d="M0 0l3 3.5L0 7M3.5 0l3 3.5-3 3.5" fill="none" stroke="#555" stroke-width="1.3"/></svg>Kitchen overhauls</li>
    </ul>
    <div class="footer-brand"><span class="dot"></span><span>The Bright Coat Inc.</span></div>
  </section>
</main>
</body>
</html>
```